Design needed for Cover of Conference Brochure

We are a conference company that puts on several business conferences per year. We are putting together a new conference - the Clearpath Forum Week, and our audience is UX practitioners and specialists, product designers, UX designers, etc.
We need a brochure cover created. We are looking for fresh design ideas and are open to varying color schemes - please just keep in mind that this is a conference for business professionals, and fonts and colors should reflect this. Only restriction is that we do have a general cover format that we follow - i.e. which text goes where. (I've attached samples from our other events to reference.) We also generally have a central image to each brochure - feel free to submit a few versions with different images... we want something that accurately represents UX. However, if the design is compelling enough, image might not be completely necessary. We are relatively flexible - we just want something sharp!
- Must include BWKT logo (see placing on sample event covers)
- Must include footer - see sample covers
- Red text in word document are notes to you the designer - not actual text meant to appear on the cover
This cover is standard 8x11, and will be used for web only, not print. I have attached a word doc that includes all of the text that you will need for the cover. We will need final version in PDF, jpeg, and PSD. Please message me with any questions or clarification.

```html
<!DOCTYPE html>
<html lang="en">
<head>
<meta charset="utf-8">
<title>Clearpath Forum Week – Brochure Cover</title>
<link rel="stylesheet" href="https://fonts.googleapis.com/css2?family=Arimo:wght@400;700&display=swap">
<style>
  :root {
    --green: #4aa52e;
    --green-light: #8fd14a;
    --green-dark: #2f8a1f;
    --blue: #1393d8;
    --blue-dark: #0b7cc0;
    --orange: #f28c28;
    --ink: #333333;
    --venue-text: #f5f2a6;
    --white: #ffffff;
    --page: #ffffff;
  }
  * { box-sizing: border-box; margin: 0; padding: 0; }
  html, body { width: 872px; height: 1200px; overflow: hidden; background: var(--page); }
  body { font-family: "Arimo", Arial, sans-serif; color: var(--ink); }
  .cover { position: relative; width: 872px; height: 1200px; overflow: hidden; background: var(--white); }

  .hero-image {
    position: absolute; left: 350px; top: 0; width: 522px; height: 520px;
    background:
      radial-gradient(ellipse at 55% 35%, #fbf6cf 0%, #e3ecd2 30%, #b9d4e6 60%, rgba(255,255,255,0) 85%),
      linear-gradient(180deg, #d9e9f2 0%, #cfe2ee 100%);
  }
  .tree-art {
    position: absolute; left: 545px; top: 690px; width: 327px; height: 400px;
    background: radial-gradient(ellipse at 55% 50%, #e3e6e8 0%, #f2f4f5 55%, rgba(255,255,255,0) 80%);
  }

  .bands { position: absolute; left: 0; top: 0; }

  .brand { position: absolute; left: 63px; top: 72px; display: flex; align-items: center; gap: 12px; }
  .brand-mark { width: 40px; height: 40px; background: var(--blue); border-radius: 6px; }
  .brand-name { font-size: 34px; font-weight: 700; color: var(--blue); letter-spacing: 1px; }

  .event-date {
    position: absolute; left: 63px; top: 210px; width: 257px; height: 48px;
    background: var(--blue); color: var(--white);
    font-size: 25px; font-weight: 700; line-height: 48px; text-align: center;
  }

  .title-main {
    position: absolute; left: 48px; top: 350px;
    font-size: 96px; font-weight: 700; line-height: 1; color: var(--white);
    letter-spacing: -2px; text-shadow: 4px 4px 6px rgba(0,0,0,0.35);
  }
  .title-sub {
    position: absolute; left: 52px; top: 492px;
    font-size: 44px; font-weight: 700; line-height: 1; color: var(--white);
    text-shadow: 2px 2px 0 #2a3a22, 3px 3px 4px rgba(0,0,0,0.4);
  }
  .tagline {
    position: absolute; left: 84px; top: 572px;
    font-size: 22px; font-weight: 700; line-height: 30px; color: var(--white);
  }

  .early-bird {
    position: absolute; left: 572px; top: 555px; width: 220px; height: 118px;
    transform: rotate(-12deg);
    font-size: 25px; font-weight: 700; line-height: 30px; color: var(--ink);
    text-align: center; padding-top: 14px;
  }
  .early-bird .amount { color: var(--blue); }

  .highlights { position: absolute; left: 87px; top: 800px; list-style: none; width: 560px; }
  .highlights li { font-size: 19px; line-height: 23px; margin-bottom: 22px; color: var(--ink); }

  .venue {
    position: absolute; left: 0; top: 1040px; width: 872px; height: 102px;
    background: var(--blue); padding: 18px 0 0 88px;
    color: var(--venue-text); font-size: 28px; font-weight: 700; line-height: 36px;
  }
  .footer {
    position: absolute; left: 0; top: 1142px; width: 872px; height: 58px;
  }
  .footer-strip {
    position: absolute; left: 0; top: 1142px; width: 872px; height: 5px; background: var(--orange);
  }
  .footer-panel {
    position: absolute; left: 0; top: 1147px; width: 872px; height: 53px;
    background: linear-gradient(100deg, var(--green-dark) 0%, var(--green) 55%, var(--green-light) 100%);
  }
</style>
</head>
<body>
<main class="cover">
  <div class="hero-image" role="img" aria-label="Photo of a professional in a white coat reaching up toward glowing digital interface icons"></div>

  <svg class="bands" width="872" height="1200" viewBox="0 0 872 1200" aria-hidden="true">
    <defs>
      <linearGradient id="greenBand" x1="0" y1="0" x2="1" y2="1">
        <stop offset="0" stop-color="#3f9a26"/>
        <stop offset="0.6" stop-color="#5fb833"/>
        <stop offset="1" stop-color="#9bd85a"/>
      </linearGradient>
      <linearGradient id="blueBand" x1="0" y1="0" x2="1" y2="0">
        <stop offset="0" stop-color="#0f8ad0"/>
        <stop offset="1" stop-color="#1aa0e6"/>
      </linearGradient>
    </defs>
    <polygon points="0,374 464,374 588,560 872,560 872,600 0,600" fill="url(#greenBand)"/>
    <polyline points="0,372 464,372 588,556 872,556" fill="none" stroke="#f28c28" stroke-width="4"/>
    <polygon points="0,600 640,600 560,690 0,690" fill="url(#blueBand)"/>
    <polygon points="0,690 560,690 640,600 872,600 872,604 646,604 566,704 0,704" fill="#5fb833"/>
    <ellipse cx="683" cy="615" rx="118" ry="62" transform="rotate(-12 683 615)" fill="#ffffff" stroke="#c8c8c8" stroke-width="2"/>
    <polygon points="640,668 610,712 672,672" fill="#ffffff" stroke="#c8c8c8" stroke-width="2" stroke-linejoin="round"/>
    <line x1="642" y1="668" x2="668" y2="670" stroke="#ffffff" stroke-width="4"/>
  </svg>

  <div class="brand">
    <span class="brand-mark"></span>
    <span class="brand-name">BWKT</span>
  </div>

  <div class="event-date">June 10 - 12, 2014</div>

  <h1 class="title-main">CLEARPATH</h1>
  <p class="title-sub">FORUM WEEK</p>

  <p class="tagline">Design Compelling Experiences<br>through Successful UX Strategy</p>

  <p class="early-bird">Register by<br>March 7th, 2014<br>and save <span class="amount">$400</span></p>

  <div class="tree-art" role="img" aria-label="Stylised grey tree with green and white flower blossoms"></div>

  <ul class="highlights">
    <li>Case Studies from Leading Brands on Executing an Effective<br>UX Strategy</li>
    <li>Learn How UX-Driven Innovation Can Change<br>Your Business</li>
    <li>Build a Successful UX Team that Operates Strategically</li>
    <li>Insights into UX Research, User Behavior, Usability<br>Testing, Lean UX, and More</li>
  </ul>

  <section class="venue">
    Harborline Club &amp; Hotel<br>San Francisco, CA
  </section>

  <div class="footer-strip"></div>
  <footer class="footer-panel">
    <svg width="872" height="53" viewBox="0 0 872 53" aria-hidden="true" style="position:absolute;left:0;top:0"></svg>
  </footer>
  <div style="position:absolute;left:88px;top:1150px;color:#fff;font-weight:700;font-size:16px;letter-spacing:6px;line-height:18px;">Register Today</div>
  <div style="position:absolute;left:88px;top:1168px;color:#fff;font-weight:700;font-size:23px;letter-spacing:3px;line-height:24px;">www.clearpathforumweek.com</div>
  <div style="position:absolute;left:88px;top:1192px;color:#fff;font-weight:700;font-size:0;"></div>
</main>
</body>
</html>
```